2nd Generation Blind Manufacturer & Retailer Needs A Stationary Set

We need a stationary set for a family business located the in the Whitsundays (QLD). We retail and manufacture blinds awnings and shutters. Second generation, in operation for over 30 years.

Final draft must include at minimum:

Business Card (2 Sided)
Letterhead
Presentation Folder

Target Market(s)

home owners, landlords, builders, real estate agents, shopping centres

Industry/Entity Type

Textile

Requirements
Must have
• Design needs to work in mono as well as colour print
Nice to have
• Relevant to the textile industry
Should not have
• The inclusion of blinds, awnings or shutters is an automatic no-no

```html
<!DOCTYPE html>
<html lang="en">
<head>
<meta charset="utf-8">
<title>Harwell Blinds – Business Card</title>
<link rel="stylesheet" href="https://fonts.googleapis.com/css2?family=Arimo:wght@400;700&display=swap">
<style>
  :root {
    --page: #e9e7e3;
    --card-white: #ffffff;
    --card-shade: #f1f1f1;
    --charcoal-top: #707070;
    --charcoal-bottom: #3f3f3f;
    --band-grey: #8a8a8a;
    --band-grey-dark: #6e6e6e;
    --teal: #1fb3ab;
    --ink: #3b3b3b;
    --brand-grey: #8c8c8c;
    --brand-light: #dcdcdc;
  }
  * { margin: 0; padding: 0; box-sizing: border-box; }
  html, body { width: 1200px; height: 950px; overflow: hidden; }
  body {
    background: var(--page);
    font-family: "Arimo", Arial, sans-serif;
    color: var(--ink);
    position: relative;
  }
  .card {
    position: absolute;
    left: 250px;
    width: 700px;
    height: 400px;
    border-radius: 4px;
    box-shadow: 0 10px 28px rgba(0,0,0,0.18);
    overflow: hidden;
  }

  /* Back side */
  .card-back {
    top: 55px;
    background: linear-gradient(160deg, var(--charcoal-top), var(--charcoal-bottom));
    display: flex;
    flex-direction: column;
    align-items: center;
    justify-content: center;
    gap: 26px;
  }
  .card-back .brand { color: var(--brand-light); }
  .card-back .brand-square { background: var(--brand-light); }
  .card-back .back-web {
    color: var(--brand-light);
    font-size: 15px;
    letter-spacing: 4px;
  }

  /* Brand lockup */
  .brand {
    display: flex;
    align-items: center;
    gap: 16px;
    color: var(--brand-grey);
    font-weight: 400;
    font-size: 36px;
    letter-spacing: 3px;
    text-transform: uppercase;
  }
  .brand-square {
    width: 46px;
    height: 46px;
    background: var(--brand-grey);
  }

  /* Front side */
  .card-front {
    top: 495px;
    background: linear-gradient(180deg, var(--card-white) 0%, var(--card-shade) 80%);
  }
  .card-front .brand {
    position: absolute;
    top: 70px;
    left: 0;
    right: 0;
    justify-content: center;
  }
  .details {
    position: absolute;
    top: 165px;
    left: 0;
    right: 0;
    display: grid;
    grid-template-columns: 1fr 1fr;
    column-gap: 40px;
  }
  .person {
    text-align: right;
    font-size: 15px;
    line-height: 21px;
  }
  .person-name {
    color: var(--teal);
    font-weight: 700;
    font-size: 19px;
    letter-spacing: 1px;
    line-height: 24px;
  }
  .person-title { margin-bottom: 2px; }
  .contacts {
    list-style: none;
    font-size: 15px;
    line-height: 21px;
    padding-top: 24px;
  }
  .contacts li { display: flex; align-items: center; gap: 8px; }
  .contacts svg { width: 13px; height: 13px; fill: var(--teal); flex: none; }
  .band {
    position: absolute;
    left: 0; right: 0; bottom: 0;
    height: 78px;
    background: linear-gradient(180deg, var(--band-grey), var(--band-grey-dark));
    border-top: 3px solid var(--teal);
    border-bottom: 3px solid var(--teal);
  }
</style>
</head>
<body>

  <section class="card card-back" aria-label="Business card, back">
    <div class="brand"><span class="brand-square"></span><span>Harwell Blinds</span></div>
    <p class="back-web">www.harwellblinds.example</p>
  </section>

  <section class="card card-front" aria-label="Business card, front">
    <div class="brand"><span class="brand-square"></span><span>Harwell Blinds</span></div>

    <div class="details">
      <div class="person">
        <p class="person-name">SAM PORTER</p>
        <p class="person-title">President</p>
        <p>1420 Harbour Lane</p>
        <p>Coral Bay, QLD 4802</p>
      </div>
      <ul class="contacts">
        <li>
          <svg viewBox="0 0 16 16" aria-hidden="true"><path d="M3 1h3l1.5 4-2 1.2a9 9 0 0 0 4.3 4.3L11 8.5l4 1.5v3a2 2 0 0 1-2 2A13 13 0 0 1 1 3a2 2 0 0 1 2-2z"/></svg>
          555 0142 7781
        </li>
        <li>
          <svg viewBox="0 0 16 16" aria-hidden="true"><path d="M4.5 0h7A1.5 1.5 0 0 1 13 1.5v13a1.5 1.5 0 0 1-1.5 1.5h-7A1.5 1.5 0 0 1 3 14.5v-13A1.5 1.5 0 0 1 4.5 0zM5 2v10h6V2zm3 11a1 1 0 1 0 0 2 1 1 0 0 0 0-2z"/></svg>
          555 0198 3364
        </li>
        <li>
          <svg viewBox="0 0 16 16" aria-hidden="true"><path d="M1 3h14v10H1zm1.5 1.2v.4L8 8.6l5.5-4v-.4z"/></svg>
          sam@harwellblinds.example
        </li>
        <li>
          <svg viewBox="0 0 16 16" aria-hidden="true"><circle cx="8" cy="8" r="7"/><circle cx="8" cy="8" r="2.5" fill="#ffffff"/></svg>
          www.harwellblinds.example
        </li>
      </ul>
    </div>

    <div class="band"></div>
  </section>

</body>
</html>
```